Redesign of an app landing page

Our page lumvexa.net needs a redesign. This would follow the typical app landing page format which we have now, that is to say a single page with some text, pictures etc. There is also a link to a seperate page with a facebook privacy policy that could use a quick polish.

I want to page to keep the minimamlistic feel that it has now but simply with a better design, a picture that fits the whole screen and the text area similar. You are free to use your design abilities to go outside this preferences if you feel the need to.

The picture in the background should show a social situation which could be anything from taking a lunch, go running, to a museum, the movies, party (no alcohol) or any other situation that we do with our friends. Our logo should be visible as well. If you need any more information, don“t hesitate to take contact

Examples of pages that I like

https://www.quandrel.tv/

http://plorvigo.io/

http://tesmik.co/

Number of Pages Required

1 page

Colors
00a990
0292cd

Requirements
Must have
• The following links need to be there with the correct logos for the pages and the download button should the most visible
• Facebook https://www.example-social.com/lumvexaprogram
• Instagram: https://www.example-photos.com/lum_vexa_kit/
• Play store: https://apps.example-store.com/store/apps/details?id=com.venture.karsido.outingkit
• There needs to be as well the facebook privacy policy link but this can be in small letters somewhere in the corner like it is now.
• http://www.lumvexa.net/#!privacy-policy/qtllt

```html
<!DOCTYPE html>
<html lang="en">
<head>
<meta charset="utf-8">
<title>lumvexa – social app</title>
<link rel="stylesheet" href="https://fonts.googleapis.com/css2?family=Comfortaa:wght@500;700&family=Lato:wght@300;400&display=swap">
<style>
  :root {
    --sky-top: #1f2d33;
    --sky-mid: #4a5a55;
    --sky-glow: #7d8a6e;
    --ground: #0d1012;
    --brand: #12a9c9;
    --panel: rgba(232, 236, 238, 0.92);
    --panel-edge: rgba(170, 180, 186, 0.85);
    --ink: #3e4447;
    --white: #ffffff;
    --button: #0b0b0b;
    --tile-1: #4f87a8;
    --tile-2: #3d6d93;
    --tile-3: #7a5b43;
  }
  * { margin: 0; padding: 0; box-sizing: border-box; }
  html, body { width: 1200px; height: 799px; overflow: hidden; }
  body { position: relative; font-family: "Lato", sans-serif; background: var(--ground); }

  .hero-photo {
    position: absolute; inset: 0;
    background:
      radial-gradient(ellipse 60% 40% at 45% 60%, rgba(125,138,110,0.55), transparent 70%),
      linear-gradient(180deg, var(--sky-top) 0%, var(--sky-mid) 55%, var(--sky-glow) 72%, var(--ground) 100%);
  }

  .app-tile {
    position: absolute; left: 285px; top: 84px; width: 127px; height: 127px;
    border-radius: 26px;
    background: linear-gradient(135deg, #8fd3e0, #1ab0cf);
  }

  .social-links { position: absolute; left: 248px; top: 308px; display: flex; gap: 20px; }
  .social-links a { display: block; width: 58px; height: 59px; border-radius: 4px; }
  .social-links .tile-checkin { background: var(--tile-1); }
  .social-links .tile-network { background: var(--tile-2); }
  .social-links .tile-photos { background: var(--tile-3); }

  .chevron { position: absolute; left: 0; top: 0; }

  .brand { font-family: "Comfortaa", sans-serif; font-weight: 700; color: var(--brand); position: absolute; white-space: nowrap; }
  .tag { font-family: "Lato", sans-serif; font-weight: 400; color: var(--brand); position: absolute; white-space: nowrap; }

  .brand-main { left: 612px; top: 92px; font-size: 92px; letter-spacing: 1px; }
  .tag-main { left: 740px; top: 198px; font-size: 26px; }
  .brand-second { left: 700px; top: 266px; font-size: 34px; font-family: "Lato", sans-serif; font-weight: 400; }
  .tag-second { left: 762px; top: 304px; font-size: 18px; }

  .features { position: absolute; color: var(--ink); font-size: 26px; font-weight: 400; white-space: nowrap; }
  .features li { list-style: none; position: absolute; }
  .features .f1 { left: 754px; top: 350px; }
  .features .f2 { left: 832px; top: 383px; }
  .features .f3 { left: 760px; top: 416px; }
  .tagline { left: 708px; top: 472px; font-size: 28px; }

  .store-button {
    position: absolute; left: 651px; top: 557px; width: 294px; height: 87px;
    background: var(--button); border-radius: 10px; border: 1px solid #555;
    color: var(--white); text-decoration: none;
  }
  .store-button .mark { position: absolute; left: 24px; top: 22px; width: 44px; height: 44px; border-radius: 50%; background: #e7e7e7; }
  .store-button .small { position: absolute; left: 94px; top: 11px; font-size: 18px; }
  .store-button .big { position: absolute; left: 92px; top: 33px; font-size: 33px; }

  .footer-brand { left: 46px; top: 588px; font-size: 40px; }
  .privacy { position: absolute; left: 54px; top: 642px; font-size: 19px; color: var(--white); text-decoration: underline; }
  .copyright { position: absolute; left: 0; right: 0; top: 755px; text-align: center; color: var(--white); font-size: 22px; }
</style>
</head>
<body>
  <div class="hero-photo" role="img" aria-label="Silhouetted group of friends tossing a person into the air against a dusky cloudy sky"></div>

  <div class="app-tile" aria-hidden="true"></div>

  <nav class="social-links" aria-label="Social links">
    <a class="tile-checkin" href="http://www.lumvexa.net" aria-label="Check-in page"></a>
    <a class="tile-network" href="https://www.example-social.com/lumvexaprogram" aria-label="Social page"></a>
    <a class="tile-photos" href="https://www.example-photos.com/lum_vexa_kit/" aria-label="Photo page"></a>
  </nav>

  <svg class="chevron" width="1200" height="799" aria-hidden="true">
    <polygon points="525,92 940,92 1130,398 940,706 525,706 717,398" fill="var(--panel-edge)"/>
    <polygon points="545,92 935,92 1120,398 935,706 545,706 737,398" fill="var(--panel)"/>
  </svg>

  <h1 class="brand brand-main">lumvexa</h1>
  <p class="tag tag-main">social app</p>
  <p class="brand brand-second">lumvexa</p>
  <p class="tag tag-second">social app</p>

  <ul class="features">
    <li class="f1">connect with friends</li>
    <li class="f2">share your activities</li>
    <li class="f3">discover your world</li>
  </ul>
  <p class="tag tagline">your social joy app</p>

  <a class="store-button" href="https://apps.example-store.com/store/apps/details?id=com.venture.karsido.outingkit">
    <span class="mark" aria-hidden="true"></span>
    <span class="small">Get it on</span>
    <span class="big">Storevia</span>
  </a>

  <p class="brand footer-brand">lumvexa</p>
  <a class="privacy" href="http://www.lumvexa.net/#!privacy-policy/qtllt">Privacy Policy</a>

  <p class="copyright">Copyright 2016 All rights Reserved. Lumvexa</p>
</body>
</html>
```